Dunmore Hale Voss LLC letterhead/envelope/stationary

Design letterhead and envelope based on prior logo design. Design should be conservative and classic for a defense litigation law firm.

Target Market(s)

Businesses, insurance carriers, construction companies, product manufacturers, healthcare providers, employers, municipalities. In short, the target is businesses that may be sued in court and need civil defense attorneys.

Font styles to use
Serif
Sans Serif

Colors
0255a3

Requirements
Must have
• Straightforward design for letterhead and envelopes including digital format for word. Template should be able to be updated for individual attorneys within the firm. Font should be Trajan Pro if possible to match logo (or a similar font). Firm information is Dunmore Hale Voss LLC, 4700 Westfield Terrace, Suite 320, Birmingham, Alabama, 35817. (205)368-2941. other fields that should be included are fax line, direct line, cell phone and email address so that we can update template for each attorney. The color for the logo is 003362
Nice to have
• digital template for microsoft outlook
Should not have
• Busy design/too many graphics

```html
<!DOCTYPE html>
<html lang="en">
<head>
<meta charset="utf-8">
<title>Dunmore Hale Voss LLC — Stationery</title>
<link rel="stylesheet" href="https://fonts.googleapis.com/css2?family=Cinzel:wght@400;600&display=swap">
<style>
  :root {
    --navy: #003362;
    --navy-deep: #0a2553;
    --blue: #0255a3;
    --paper: #ffffff;
    --envelope-back: #eef0f3;
    --backdrop: #e4e6e9;
    --ink-grey: #5a5f66;
  }
  * { margin: 0; padding: 0; box-sizing: border-box; }
  html, body { width: 1187px; height: 1200px; overflow: hidden; }
  body {
    background: var(--backdrop);
    font-family: "Cinzel", "Times New Roman", serif;
    position: relative;
  }
  .letterhead {
    position: absolute; left: 60px; top: 105px;
    width: 700px; height: 990px;
    background: var(--paper);
    box-shadow: 0 6px 20px rgba(0,0,0,.12);
    overflow: hidden;
  }
  .letterhead__bands { position: absolute; inset: 0; width: 100%; height: 100%; }
  .firm-mark { position: absolute; color: var(--navy); white-space: nowrap; }
  .firm-mark__name { font-weight: 600; letter-spacing: .04em; line-height: 1.1; }
  .firm-mark__tagline { font-weight: 600; letter-spacing: .18em; }
  .letterhead .firm-mark { left: 42px; top: 124px; }
  .letterhead .firm-mark__name { font-size: 20px; }
  .letterhead .firm-mark__tagline { font-size: 8.5px; margin-top: 4px; }
  .letterhead__footer {
    position: absolute; right: 48px; bottom: 118px;
    text-align: center; color: var(--ink-grey);
    font-size: 12.5px; line-height: 1.65; letter-spacing: .03em;
    font-style: normal;
  }
  .letterhead__footer .email { color: var(--blue); }

  .envelope {
    position: absolute; left: 795px; width: 360px; height: 200px;
    box-shadow: 0 5px 16px rgba(0,0,0,.12);
    overflow: hidden;
  }
  .envelope--back { top: 400px; background: var(--envelope-back); }
  .envelope--front { top: 640px; background: var(--paper); }
  .envelope svg { position: absolute; inset: 0; width: 100%; height: 100%; }
  .envelope .firm-mark { left: 14px; top: 22px; }
  .envelope .firm-mark__name { font-size: 8.5px; }
  .envelope .firm-mark__tagline { font-size: 4.5px; margin-top: 2px; }
  .envelope__contact {
    position: absolute; left: 14px; top: 48px;
    list-style: none; color: var(--ink-grey);
    font-size: 5.5px; line-height: 1.6; letter-spacing: .03em;
  }
  .envelope__contact li::before {
    content: ""; display: inline-block; width: 4px; height: 4px;
    border-radius: 50%; background: var(--blue); margin-right: 4px; vertical-align: middle;
  }
</style>
</head>
<body>

<section class="letterhead" aria-label="Letterhead">
  <svg class="letterhead__bands" viewBox="0 0 700 990" preserveAspectRatio="none" aria-hidden="true">
    <polygon points="0,0 688,0 545,122 0,22" fill="var(--navy-deep)"/>
    <polygon points="0,30 548,134 700,4 700,18 556,150 0,42" fill="var(--blue)"/>
    <polygon points="0,932 700,878 700,892 0,947" fill="var(--blue)"/>
    <polygon points="0,958 700,904 700,990 0,990" fill="var(--navy-deep)"/>
  </svg>
  <div class="firm-mark">
    <div class="firm-mark__name">Dunmore Hale Voss LLC</div>
    <div class="firm-mark__tagline">Attorneys at Law</div>
  </div>
  <address class="letterhead__footer">
    4700 Westfield Terrace, Suite 320, Birmingham, Alabama, 35817<br>
    (205)368-2941 | (205)368-2942 | (205)368-2950<br>
    <span class="email">info@dunmorehalevoss.com</span>
  </address>
</section>

<section class="envelope envelope--back" aria-label="Envelope back">
  <svg viewBox="0 0 360 200" preserveAspectRatio="none" aria-hidden="true">
    <polygon points="0,0 360,0 360,30 190,118 170,118 0,30" fill="var(--navy-deep)"/>
  </svg>
</section>

<section class="envelope envelope--front" aria-label="Envelope front">
  <svg viewBox="0 0 360 200" preserveAspectRatio="none" aria-hidden="true">
    <polygon points="190,0 360,0 360,150 296,146" fill="var(--navy-deep)"/>
    <polygon points="168,0 180,0 292,154 360,158 360,166 284,162" fill="var(--blue)"/>
  </svg>
  <div class="firm-mark">
    <div class="firm-mark__name">Dunmore Hale Voss LLC</div>
    <div class="firm-mark__tagline">Attorneys at Law</div>
  </div>
  <ul class="envelope__contact">
    <li>(205)368-2941</li>
    <li>(205)368-2942</li>
    <li>(205)368-2950</li>
    <li>info@dunmorehalevoss.com</li>
    <li>4700 Westfield Terrace, Suite 320</li>
    <li>Birmingham, Alabama, 35817</li>
  </ul>
</section>

</body>
</html>
```